Looking for a unique designer to design new & exciting stationery for progressive professional firm

Hello! We would like to stand out, but in a good way. We want a modern unique image, something creative, but remain professional. Also portray integrity and look approachable. We want to appeal to the younger generation while not losing the respect of our more conservative older clients!

Our focus at Lantern Partners is on guiding our clients and assisting them to 'keep your books in order'. We are a small boutique accounting firm based in Melbourne Australia.

Using our 2 distinctive colours (blue & yellow) and new logo design attached, please design a modern and professional letterhead, with compliments slip and business card for our firm.

The necessary words and logos to be included on the letterhead and card are attached, the overall design of the stationery however is up to your talent. Font to be modern, professional & progressive! I like the font style (MS words Trebuchet MS) on my draft letterhead design attached. It looks modern, professional but approachable so something like that would be great.

For the business card, I like the attached version's REAR side of the business card but not the front side, so please come up with a design for the front that will match the letterhead design you come up with. I don't like how the company name sits tightly below the logo, they make the logo look too large in proportion to the words. Also feel free to change the rear side if you believe you have a better design :)

The colours are blue R31 G125 B165
and yellow R224 G201 B24, but please convert to CMYK equivalent.

At full sizing for the card, withcomps slip and letterhead respectively, the images need to be at least 300 dpi or higher.

Please advise if you need any other files (eg for higher resolution) or information and/or refer to our website for further input.

Thank you, with great anticipation...

Dylan

Target Market(s)

Discerning (and wealthy?) clients, both business owners and personal, looking for a progressive, approachable but professional accounting firm. Need to attract and appeal to the younger generations while not losing the respect of the older more conservative generation.

Industry/Entity Type

Accounting

Font styles to use
Other font styles liked:
• Something like MW word's Trebuchet MS - for company name. Happy for you to suggest other font for other wording.

Requirements
Must have
• My company logo, QBT logo, the wording I have included on the sample of letterhead and business card.
• The colours are blue R31 G125 B165 and yellow R224 G201 B24, but please convert to CMYK equivalent. Also use a grey for smaller wording. Refer sample letterhead attached. Note that the blue and yellow on the QBT logo are not the same as the my blue and yellow above. They will and should look different.
• Note: QBT logo must have a space around it of at least half the width of the yellow part of the logo - per my attached letter sample. The logo must be at least 15mm in width on all stationery. Also the QBT logo must have the words adjacent to it, 'Lantern Partners Pty Ltd is a QBT practice'.
Nice to have
• Maybe curved features at bottom and/or top of letterhead instead of the rectangle coloured bars that my sample letter has.
• Good to maybe have Icons for telephone, fax email address etc.
Should not have
• No other colours except my blue, yellow and black, grey and white.
• No detailed pictures as I want to keep the design modern, minimalistic and flat.

```html
<!DOCTYPE html>
<html lang="en">
<head>
<meta charset="utf-8">
<title>Lantern Partners – Stationery</title>
<link rel="stylesheet" href="https://fonts.googleapis.com/css2?family=Fira+Sans:ital,wght@0,400;0,500;0,600;1,400&display=swap">
<style>
:root{
  --blue:#4672a6;
  --blue-deep:#2f5f97;
  --yellow:#d6c331;
  --grey-band:#dedede;
  --paper:#f6f6f6;
  --ink:#3c3c3c;
  --muted:#777;
  --bg:#d2d2d4;
}
*{box-sizing:border-box;margin:0;padding:0}
html,body{width:1200px;height:991px;overflow:hidden}
body{background:var(--bg);font-family:"Fira Sans",sans-serif;color:var(--ink);position:relative}
.piece{position:absolute;background:var(--paper);overflow:hidden}
.wave{position:absolute;left:0;bottom:0;width:100%}
.mark{position:absolute;display:flex;align-items:center;gap:8px}
.mark .dot{border-radius:50%;background:var(--blue);flex:none}
.mark .name{color:var(--blue);font-weight:600;line-height:1.02;letter-spacing:.02em}
.tagline{font-style:italic;color:var(--muted);display:block;font-weight:400;letter-spacing:0}
.contact{position:absolute;font-size:5.6px;color:var(--ink);line-height:1.35}
.contact li{list-style:none;display:flex;align-items:center;gap:3px}
.contact .ico{width:5px;height:5px;background:var(--blue);border-radius:1px;flex:none}
.badge{position:absolute;background:var(--yellow);border:1.5px solid var(--blue)}
.faint{position:absolute;border-radius:50%}

/* letterhead */
.letterhead{left:71px;top:103px;width:398px;height:562px}
.letterhead .mark{left:38px;top:30px}
.letterhead .dot{width:42px;height:42px}
.letterhead .name{font-size:13px}
.letterhead .tagline{font-size:5px;margin-top:2px}
.letterhead .contact{left:286px;top:36px}
.letterhead .address{margin-top:6px;display:block}
.letterhead .legal{position:absolute;left:288px;top:529px;font-size:4.2px;color:var(--ink);text-align:right;width:50px;line-height:1.3}
.letterhead .badge{left:344px;top:527px;width:30px;height:12px}
.letterhead .liability{position:absolute;left:80px;bottom:3px;width:180px;font-size:4.2px;color:#fff;text-align:center;line-height:1.3}

/* presentation folder */
.folder{left:507px;top:90px;width:433px;height:576px}
.folder .spine{position:absolute;left:26px;top:0;width:1px;height:100%;background:rgba(0,0,0,.07)}
.folder .mark{left:135px;top:70px;gap:10px}
.folder .dot{width:62px;height:62px}
.folder .name{font-size:18.5px}
.folder .tagline{font-size:7.5px;margin-top:3px}
.folder .cover{position:absolute;left:0;top:178px;width:100%;height:398px}
.folder .faint{left:93px;top:244px;width:248px;height:248px;background:rgba(255,255,255,.06)}
.folder .services{position:absolute;left:0;width:100%;top:691px;text-align:center}
.folder .line{position:absolute;left:0;width:100%;top:533px;text-align:center;color:var(--yellow);font-size:10.5px;font-weight:500;letter-spacing:.05em}

/* business card front */
.card-front{left:67px;top:696px;width:170px;height:95px}
.card-front .person{position:absolute;left:10px;top:21px;font-size:5px;color:var(--blue-deep);font-weight:600;line-height:1.3}
.card-front .person small{display:block;font-weight:400;color:var(--muted);font-size:4px}
.card-front .mark{left:100px;top:14px;gap:4px}
.card-front .dot{width:22px;height:22px}
.card-front .name{font-size:7.5px}
.card-front .tagline{font-size:3px;margin-top:1px}
.card-front .contact{left:10px;top:62px;font-size:4px;color:#fff}
.card-front .contact .ico{width:3.5px;height:3.5px;background:var(--yellow)}
.card-front .addr{position:absolute;right:10px;top:72px;font-size:4px;color:#fff;text-align:right;line-height:1.35}

/* business card back */
.card-back{left:67px;top:810px;width:170px;height:95px;background:var(--blue)}
.card-back .faint{left:104px;top:-2px;width:64px;height:64px;background:rgba(255,255,255,.06)}
.card-back .mark{left:13px;top:20px;gap:6px}
.card-back .dot{width:30px;height:30px;background:var(--yellow)}
.card-back .name{font-size:10px;color:#fff}
.card-back .tagline{font-size:3.5px;color:#e8e8e8;margin-top:1px}
.card-back .strip{position:absolute;left:0;bottom:5px;width:100%;height:24px;background:#fff}
.card-back .badge{left:13px;top:6px;width:30px;height:12px}
.card-back .legal{position:absolute;left:48px;top:7px;font-size:3.6px;color:var(--ink);line-height:1.3}
.card-back .services{position:absolute;right:12px;top:6px;font-size:4.6px;color:var(--blue-deep);font-weight:600;text-align:right;line-height:1.2}

/* compliments slip */
.slip{left:266px;top:696px;width:415px;height:209px}
.slip .mark{left:21px;top:26px;gap:6px}
.slip .dot{width:42px;height:42px}
.slip .name{font-size:12.5px}
.slip .tagline{font-size:4.8px;margin-top:2px}
.slip .faint{left:206px;top:26px;width:172px;height:172px;background:rgba(0,0,0,.025)}
.slip .address{position:absolute;left:21px;top:173px;font-size:5.6px;line-height:1.35}

/* envelope */
.envelope{left:718px;top:696px;width:415px;height:209px}
.envelope .flap{position:absolute;left:0;top:0;width:100%;height:58px}
.envelope .seal{position:absolute;left:193px;top:17px;width:29px;height:29px;border-radius:50%;background:var(--yellow);border:2px solid #fff}
.envelope .web{position:absolute;left:0;width:100%;top:180px;text-align:center;font-size:5.6px;color:var(--ink)}
</style>
</head>
<body>

<section class="piece letterhead" aria-label="Letterhead">
  <div class="mark"><span class="dot"></span><div class="name">LANTERN<br>PARTNERS<span class="tagline">Keep Your Books In Order</span></div></div>
  <ul class="contact">
    <li><span class="ico"></span>+61 3 9000 4120</li>
    <li><span class="ico"></span>+61 3 9000 4121</li>
    <li><span class="ico"></span>hello@lanternpartners.net.au</li>
    <li><span class="ico"></span>www.lanternpartners.net.au</li>
    <li class="address">Suite 14, 8 Harbour Lane<br>Kew Victoria 3101</li>
  </ul>
  <p class="legal">Lantern Partners Pty Ltd is a QBT Practice</p>
  <span class="badge"></span>
  <svg class="wave" viewBox="0 0 400 36" height="36" preserveAspectRatio="none" aria-hidden="true">
    <path d="M0 24 C120 0 260 4 400 14 L400 36 L0 36Z" fill="var(--yellow)"/>
    <path d="M0 28 C130 6 260 10 400 20 L400 36 L0 36Z" fill="var(--grey-band)"/>
    <path d="M0 32 C140 12 250 18 330 36 L0 36Z" fill="var(--blue)"/>
  </svg>
  <p class="liability">Liability limited by a scheme approved under<br>Professional Standards Legislation · ABN 00 000 000 000</p>
</section>

<section class="piece folder" aria-label="Presentation folder">
  <span class="spine"></span>
  <div class="mark"><span class="dot"></span><div class="name">LANTERN<br>PARTNERS<span class="tagline">Keep Your Books In Order</span></div></div>
  <svg class="cover" viewBox="0 0 433 398" preserveAspectRatio="none" aria-hidden="true">
    <path d="M0 22 C140 -10 300 0 433 18 L433 398 L0 398Z" fill="var(--yellow)"/>
    <path d="M0 34 C150 0 300 10 433 30 L433 398 L0 398Z" fill="var(--grey-band)"/>
    <path d="M0 42 C150 8 290 18 433 44 L433 398 L0 398Z" fill="var(--blue)"/>
  </svg>
  <span class="faint"></span>
  <p class="line">ACCOUNTANTS &amp; BUSINESS ADVISORS</p>
</section>

<section class="piece card-front" aria-label="Business card front">
  <p class="person">DYLAN ASHBY<small>Director</small></p>
  <div class="mark"><span class="dot"></span><div class="name">LANTERN<br>PARTNERS<span class="tagline">Keep Your Books In Order</span></div></div>
  <svg class="wave" viewBox="0 0 170 56" height="56" preserveAspectRatio="none" aria-hidden="true">
    <path d="M0 0 C60 -2 120 4 170 14 L170 56 L0 56Z" fill="var(--yellow)"/>
    <path d="M0 4 C60 2 120 8 170 18 L170 56 L0 56Z" fill="var(--grey-band)"/>
    <path d="M0 8 C60 6 120 12 170 22 L170 56 L0 56Z" fill="var(--blue)"/>
  </svg>
  <ul class="contact">
    <li><span class="ico"></span>+61 3 9000 4120</li>
    <li><span class="ico"></span>+61 3 9000 4121</li>
    <li><span class="ico"></span>hello@lanternpartners.net.au</li>
    <li><span class="ico"></span>www.lanternpartners.net.au</li>
  </ul>
  <p class="addr">Suite 14<br>8 Harbour Lane<br>Kew Victoria 3101</p>
</section>

<section class="piece card-back" aria-label="Business card back">
  <span class="faint"></span>
  <div class="mark"><span class="dot"></span><div class="name">LANTERN<br>PARTNERS<span class="tagline">Keep Your Books In Order</span></div></div>
  <div class="strip">
    <span class="badge"></span>
    <p class="legal">Lantern Partners Pty Ltd<br>is a QBT Practice</p>
    <p class="services">ACCOUNTANTS &amp;<br>BUSINESS ADVISORS</p>
  </div>
</section>

<section class="piece slip" aria-label="Compliments slip">
  <span class="faint"></span>
  <div class="mark"><span class="dot"></span><div class="name">LANTERN<br>PARTNERS<span class="tagline">Keep Your Books In Order</span></div></div>
  <p class="address">Suite 14, 8 Harbour Lane<br>Kew Victoria 3101</p>
  <svg class="wave" viewBox="0 0 415 34" height="34" preserveAspectRatio="none" aria-hidden="true">
    <path d="M0 22 C150 2 300 0 415 10 L415 34 L0 34Z" fill="var(--yellow)"/>
    <path d="M0 26 C150 6 300 4 415 16 L415 34 L0 34Z" fill="var(--grey-band)"/>
    <path d="M150 34 C230 12 330 10 415 22 L415 34Z" fill="var(--blue)"/>
    <path d="M0 30 C60 26 110 26 150 34 L0 34Z" fill="var(--yellow)"/>
  </svg>
</section>

<section class="piece envelope" aria-label="Envelope">
  <svg class="flap" viewBox="0 0 415 58" preserveAspectRatio="none" aria-hidden="true">
    <path d="M0 0 L415 0 L400 48 Q398 58 388 58 L27 58 Q17 58 15 48Z" fill="var(--blue)"/>
  </svg>
  <span class="seal"></span>
  <p class="web">www.lanternpartners.net.au</p>
</section>

</body>
</html>
```